Business Card Design for a Personal Trainer

I need a business card design for my job as a personal trainer. It should have a unique, modern and exclusive design. On the front there should be only my logo with my name and my job. 0163/2918374 Tobias Kellinger Lindenfeldweg 14 80412 Munich Germany The most important contact information is the web adress. it can be bigger than the rest, but its not necessary. The card should be 8,5cmx5,5cm big. Font: Roboto. Colors: black, white, gray, 56c1ff.

```html
<!DOCTYPE html>
<html lang="de">
<head>
<meta charset="utf-8">
<title>Tobias Kellinger – Personal Trainer Visitenkarte</title>
<link href="https://fonts.googleapis.com/css2?family=Roboto:wght@300;400&family=Bebas+Neue&display=swap" rel="stylesheet">
<style>
  :root {
    --backdrop: #5b5b5b;
    --card: #3c3c3c;
    --ink: #ffffff;
    --rule: #d8d8d8;
    --photo-light: #8a8a8a;
    --photo-dark: #1e1e1e;
  }
  html, body {
    margin: 0;
    width: 1200px;
    height: 1200px;
    overflow: hidden;
    background: var(--backdrop);
  }
  .canvas { position: relative; width: 1200px; height: 1200px; }
  .card {
    position: absolute;
    top: 196px;
    width: 462px;
    height: 810px;
    background: var(--card);
    overflow: hidden;
    font-family: "Roboto", sans-serif;
    color: var(--ink);
  }
  .card--front { left: 77px; }
  .card--back { left: 658px; }

  .brand {
    position: absolute;
    top: 212px;
    left: 0;
    right: 0;
    text-align: center;
  }
  .brand__name {
    font-weight: 300;
    font-size: 36px;
    letter-spacing: 0.5px;
    line-height: 1;
    text-transform: uppercase;
  }
  .brand__role {
    display: flex;
    align-items: center;
    justify-content: center;
    gap: 8px;
    margin-top: 8px;
    font-weight: 400;
    font-size: 12.5px;
    letter-spacing: 3.6px;
    text-transform: uppercase;
  }
  .brand__role::before,
  .brand__role::after {
    content: "";
    width: 54px;
    height: 1px;
    background: var(--rule);
  }

  .contact {
    position: absolute;
    left: 67px;
    top: 524px;
    margin: 0;
    padding: 0;
    list-style: none;
    font-weight: 300;
    font-size: 20.5px;
    letter-spacing: 0.6px;
    line-height: 1.4;
  }
  .contact__item {
    padding-bottom: 6px;
    margin-bottom: 7px;
    border-bottom: 1px solid var(--rule);
  }
  .contact__item--phone { width: 182px; }
  .contact__item--mail { width: 336px; }
  .contact__item--web { width: 288px; }
  .contact__item--address { width: 182px; position: relative; }
  .contact__item--address::after {
    content: "";
    position: absolute;
    left: 0;
    bottom: -6px;
    width: 20px;
    height: 5px;
    background: var(--ink);
  }

  .portrait {
    position: absolute;
    left: 0;
    top: 12px;
    width: 342px;
    bottom: 0;
    background: radial-gradient(ellipse at 45% 25%, var(--photo-light) 0%, #4a4a4a 45%, var(--photo-dark) 100%);
  }
  .vertical-name {
    position: absolute;
    left: 374px;
    bottom: 30px;
    writing-mode: vertical-rl;
    transform: rotate(180deg);
    font-family: "Bebas Neue", "Roboto", sans-serif;
    font-size: 64px;
    line-height: 1;
    letter-spacing: 1px;
    white-space: nowrap;
  }
</style>
</head>
<body>
<main class="canvas">
  <section class="card card--front">
    <header class="brand">
      <div class="brand__name">Tobias Kellinger</div>
      <div class="brand__role">Personal Trainer</div>
    </header>
    <ul class="contact">
      <li class="contact__item contact__item--phone">+0163/2918374</li>
      <li class="contact__item contact__item--mail">training@tobiaskellinger.de</li>
      <li class="contact__item contact__item--web">www.tobiaskellinger.de</li>
      <li class="contact__item contact__item--address">Lindenfeldweg 14<br>80412 München</li>
    </ul>
  </section>

  <section class="card card--back">
    <div class="portrait" role="img" aria-label="Schwarz-weiß Porträtfoto des Trainers mit verschränkten Armen im Sportshirt"></div>
    <div class="vertical-name">Tobias Kellinger</div>
  </section>
</main>
</body>
</html>
```